Purchasing Management Consulting B to B Web Design PAYMENT GUARANTY

We'd like to build a new digital image for our website.

Our company is managing purchasing consultancy services for Large and Medium companies around 4 activities :
- Procurement outsourcing
- Purchasing consulting (cost reduction)
- Supply chain training
- Web platform to manage Supplier risk (TrovaNorm.com)

We now aim to harmonies our website in term of design in order to build a strongest Corporate Image.

SEE REQUIREMENT ENCLOSED

Please have a look on our current websites:
- www.kelpstrand.com
- www.qtr-network.com
- www.trovanorm.com

Reason: Hello, Some project received are not really professional and need more details. I did not see all deliverable requested in specifications. I'll revert to designer to improve design. Regards, Gaspard

Reason: Only few designers reply and feedback still need to be done.

Target Market(s)

Our business is exclusively Business to Business toward Medium and Large companies.

Industry/Entity Type

Digital

Requirements
Must have
• Website will be developped in Joomla CMS.
The user community will use Jomsocial module : Visitor should be "influenced" to communicate its contact details by registering the community.

Ergonomy, Simplicity and professionnalism is the key objectives.

Deliverables :
- Corporate Home page including clear access to our 4 activities
- Dynamique banner
- Corporate article / contact pages (1 or 2)
- Activities home pages (x 4)
- Activity Catalog (Indesign for paper version)
Nice to have
• Integration of Design for our consulting and training catalog will be interesting.

Livechat design (the one of Pixelharbor.com is good)
Should not have
• Only psd

Not html

```html
<!DOCTYPE html>
<html lang="en">
<head>
<meta charset="utf-8">
<title>KSN Consulting</title>
<link rel="stylesheet" href="https://fonts.googleapis.com/css2?family=Roboto:wght@300;400;700&display=swap">
<style>
:root{
  --lime:#d3d600;
  --amber:#f6c21b;
  --mid-grey:#7b7b7c;
  --dark-grey:#3e3e3e;
  --nav-grey:#9a9a9a;
  --brand-grey:#6e6e6e;
  --text-light:#f1f1f1;
  --text-muted:#b9b9b9;
  --footer-bg:#f3f3f3;
}
*{margin:0;padding:0;box-sizing:border-box}
html,body{width:1200px;height:1091px;overflow:hidden}
body{font-family:"Roboto",Arial,sans-serif;background:#fff;position:relative;color:#333}
.abs{position:absolute}
.backdrop{left:0;top:0;width:1200px;height:1091px}

/* header */
.brand{left:200px;top:52px;display:flex;align-items:center;gap:8px;white-space:nowrap}
.brand-square{width:14px;height:14px;background:var(--amber);display:block}
.brand-name{font-size:20px;font-weight:400;color:var(--brand-grey)}
.lang{left:857px;top:17px;font-size:10px;color:#777;display:flex;align-items:center;gap:3px;white-space:nowrap}
.lang-select{width:64px;height:14px;border:1px solid #ccc;background:#fff;color:var(--amber);font-size:10px;padding-left:3px;position:relative;line-height:12px}
.lang-select::after{content:"";position:absolute;right:0;top:0;width:12px;height:12px;background:var(--amber)}
.login{left:694px;top:38px;display:flex;gap:2px}
.field{height:19px;border:1px solid #bbb;background:#fff;font-size:10px;color:#aaa;padding:3px 5px;white-space:nowrap}
.btn-small{height:19px;font-size:10px;color:#444;padding:3px 0;text-align:center;white-space:nowrap}
.nav{left:440px;top:92px;display:flex;align-items:center;font-size:17px;font-weight:300;color:var(--nav-grey);white-space:nowrap}
.nav a{color:inherit;text-decoration:none}
.nav .sep{width:1px;height:12px;border-left:1px dashed #999;margin:0 24px}
.nav .current{color:var(--amber)}
.home-icon{left:449px;top:73px}

/* hero */
.map-area{left:200px;top:135px;width:360px;height:360px;background:radial-gradient(ellipse at center,rgba(200,200,200,.35),rgba(255,255,255,0) 70%)}
.hero-photo{left:585px;top:148px;width:415px;height:375px;border-radius:40% 8% 30% 10%;
  background:radial-gradient(ellipse at 55% 45%,#3a5680 0%,#50698c 35%,#d9dee6 70%,rgba(255,255,255,0) 100%)}
.headline{left:200px;top:256px;width:356px}
.line1{position:absolute;left:0;top:0;width:356px;height:46px;background:var(--lime);text-align:right;padding-right:4px;line-height:46px;white-space:nowrap}
.line2{position:absolute;left:153px;top:48px;width:203px;height:46px;background:var(--amber);text-align:right;padding-right:4px;line-height:46px;white-space:nowrap}
.thin{font-weight:300;font-size:30px;color:#333}
.bold{font-weight:700;font-size:38px;color:#111}
.line3{position:absolute;right:4px;top:96px;font-weight:300;font-size:33px;color:#111;white-space:nowrap}
.slider-arrows{left:920px;top:524px;display:flex;gap:1px}
.slider-arrows span{width:40px;height:35px;background:var(--amber);display:flex;align-items:center;justify-content:center}

/* welcome */
.welcome-title{left:0;top:566px;width:1200px;text-align:center;font-size:32px;font-weight:300;color:#fff;white-space:nowrap}
.welcome-title strong{font-weight:700;background:linear-gradient(90deg,var(--lime),var(--amber));-webkit-background-clip:text;background-clip:text;color:transparent}
.welcome-text{left:200px;top:619px;width:800px;font-size:11.4px;line-height:17.6px;font-weight:300;color:var(--text-light)}
.btn-read{background:var(--amber);color:#fff;font-size:12px;font-weight:300;text-align:center;line-height:26px;white-space:nowrap}
.welcome-more{left:200px;top:743px;width:78px;height:26px}

/* footer columns */
.col-title{font-size:20px;font-weight:300;color:var(--lime);white-space:nowrap}
.col-title b{font-weight:700}
.newsletter-title{left:200px;top:835px;width:278px;text-align:center}
.newsletter-text{left:200px;top:876px;width:278px;text-align:center;font-size:9.5px;line-height:14.5px;color:var(--text-muted)}
.newsletter-form{left:200px;top:914px;width:279px;height:39px;background:#fff;border:1px solid #ccc;border-radius:3px}
.newsletter-input{position:absolute;left:6px;top:5px;width:202px;height:28px;border:1px solid #ccc;font-size:9px;color:#555;padding:9px 7px}
.newsletter-btn{position:absolute;left:215px;top:5px;width:57px;height:28px;background:var(--amber);font-size:9px;color:#333;text-align:center;line-height:28px;white-space:nowrap}
.social{left:200px;top:971px;display:flex;gap:8px}
.social span{width:29px;height:29px;border-radius:50%;background:var(--amber)}
.intro-title{left:565px;top:835px;width:172px;text-align:center}
.intro-text{left:565px;top:876px;width:190px;font-size:10px;line-height:16px;color:#fff}
.intro-more{left:565px;top:974px;width:78px;height:26px}
.news-title{left:827px;top:838px}
.news-item{left:829px;display:flex;gap:13px}
.date-box{width:30px;height:30px;border:2px solid #ddd;color:#ddd;font-size:7px;text-align:center;line-height:9px;padding-top:5px}
.news-text{font-size:10px;line-height:13px;color:var(--text-muted);letter-spacing:.4px;padding-top:2px;white-space:nowrap}

/* bottom bar */
.copyright{left:200px;top:1055px;font-size:10px;color:#999;letter-spacing:.3px;white-space:nowrap}
.copyright span{color:#333}
.footer-brand{left:955px;top:1045px;display:flex;align-items:center;gap:4px;font-size:12px;font-weight:700;color:#999}
.footer-brand i{width:20px;height:20px;border-radius:50%;background:#ccc;display:block}
</style>
</head>
<body>

<svg class="abs backdrop" viewBox="0 0 1200 1091" aria-hidden="true">
  <defs>
    <linearGradient id="sky" x1="0" y1="0" x2="0" y2="1">
      <stop offset="0" stop-color="#ffffff"/>
      <stop offset="1" stop-color="#e4e4e4"/>
    </linearGradient>
  </defs>
  <rect width="1200" height="540" fill="url(#sky)"/>
  <polygon points="0,464 1200,532 1200,760 0,832" fill="var(--mid-grey)"/>
  <polygon points="0,832 1200,750 1200,1032 0,1032" fill="var(--dark-grey)"/>
  <rect y="1032" width="1200" height="59" fill="var(--footer-bg)"/>
</svg>

<div class="abs map-area" role="img" aria-label="Faint dotted world map with city skyline silhouette"></div>
<div class="abs hero-photo" role="img" aria-label="Photo of three business people around a laptop at a white desk"></div>

<header>
  <div class="abs brand">
    <span class="brand-square"></span>
    <span class="brand-name">KSN Consulting</span>
  </div>
  <div class="abs lang">Select Language: <span class="lang-select">English</span></div>
  <div class="abs login">
    <span class="field" style="width:107px">User name or Email</span>
    <span class="field" style="width:108px">Password</span>
    <span class="btn-small" style="width:43px;background:var(--lime)">Sign Up</span>
    <span class="btn-small" style="width:43px;background:var(--amber)">Login</span>
  </div>
  <svg class="abs home-icon" width="24" height="20" viewBox="0 0 24 20" aria-hidden="true">
    <polygon points="12,1 23,10 20,10 20,19 14,19 14,13 10,13 10,19 4,19 4,10 1,10" fill="var(--lime)"/>
  </svg>
  <nav class="abs nav">
    <a class="current" href="#">Home</a><span class="sep"></span>
    <a href="#">Kelp strand</a><span class="sep"></span>
    <a href="#">Services</a><span class="sep"></span>
    <a href="#">Consultancy</a><span class="sep"></span>
    <a href="#">Contact Us</a>
  </nav>
</header>

<section class="abs headline">
  <div class="line1"><span class="thin">You Will Have </span><span class="bold">Definitely</span></div>
  <div class="line2"><span class="thin">A Good </span><span class="bold">Start</span></div>
  <div class="line3">With Us!</div>
</section>

<div class="abs slider-arrows">
  <span><svg width="14" height="20" viewBox="0 0 14 20"><polyline points="11,2 3,10 11,18" fill="none" stroke="#444" stroke-width="1.5"/></svg></span>
  <span><svg width="14" height="20" viewBox="0 0 14 20"><polyline points="3,2 11,10 3,18" fill="none" stroke="#444" stroke-width="1.5"/></svg></span>
</div>

<section>
  <h1 class="abs welcome-title">Welcome to <strong>KSN CONSULTING</strong></h1>
  <p class="abs welcome-text">Lorem ipsum dolor sit amet, consectetur adipiscing elit. Donec vel risus mauris. Proin dapibus egestas est, a lacinia nisi vestibulum eu. Sed congue elit a purus accumsan eu ornare mi bibendum. Curabitur placerat justo sit amet velit volutpat id sagittis lectus accumsan. Maecenas nisl odio, convallis non pulvinar eu, rutrum a ligula. Praesent fringilla ultrices nisi sit amet placerat. Aliquam nibh eros, porttitor ac iaculis ut, semper in leo. Phasellus turpis mi, dictum id lacinia in, posuere at diam. Praesent accumsan elementum gravida. eu ornare mi bibendum. Curabitur placerat justo sit amet velit volutpat id sagittis lectus accumsan. Maecenas nisl odio, convallis non pulvinar eu, rutrum a ligula. Praesent fringilla ultrices nisi sit amet placerat. Aliquam nibh eros, porttitor.</p>
  <div class="abs btn-read welcome-more">Read More...</div>
</section>

<section>
  <h2 class="abs col-title newsletter-title">Newsletter <b>Sign Up</b></h2>
  <p class="abs newsletter-text">Want to keep up to date with all our latest news and information?<br>Enter your email below to be added to our mailing list.</p>
  <div class="abs newsletter-form">
    <span class="newsletter-input">Email Address</span>
    <span class="newsletter-btn">Sign Up</span>
  </div>
  <div class="abs social"><span></span><span></span><span></span><span></span></div>
</section>

<section>
  <h2 class="abs col-title intro-title">Introduction</h2>
  <p class="abs intro-text">Lorem ipsum dolor sit amet, consectetur adipiscing elit. Donec vel risus mauris. Proin dapibus egestas est, a lacinia nisi vestibulum Sed congue.</p>
  <div class="abs btn-read intro-more">Read More...</div>
</section>

<section>
  <h2 class="abs col-title news-title">News Artical</h2>
  <div class="abs news-item" style="top:879px"><div class="date-box">10<br>May</div><p class="news-text">Lorem ipsum dolor sit amet,<br>consectetur adipiscing elit.</p></div>
  <div class="abs news-item" style="top:925px"><div class="date-box">10<br>May</div><p class="news-text">Lorem ipsum dolor sit amet,<br>consectetur adipiscing elit.</p></div>
  <div class="abs news-item" style="top:970px"><div class="date-box">10<br>May</div><p class="news-text">Lorem ipsum dolor sit amet,<br>consectetur adipiscing elit.</p></div>
</section>

<footer>
  <p class="abs copyright">Copyright © 2008-2013 <span>KSN CONSULTING.</span> All rights reserved.</p>
  <div class="abs footer-brand"><i></i>KSN</div>
</footer>

</body>
</html>
```